Webdesign für Beratung zu Themen der Qualität und Nachhaltigkeit
Zielgruppe
Ich werde mich ab 1.1.23 selbständig machen mit der Beratung zu Themen der Qualität und Nachhaltigkeit. Meine Zielgruppe sind Bildungsinstitutionen, insbesondere Volkshochschulen.
Die Webseite richtet sich an das Management von Bildungseinrichtungen.
Aufgabenstellung
Ich habe bereits eine Visitenkarte, an deren Design sich orientiert werden kann. Ich habe dieses über ein Visitenkarten-Tool erstellen lassen und besitze keine Daten dazu. Ein Foto hänge ich an.

```html
<!DOCTYPE html>
<html lang="de">
<head>
<meta charset="utf-8">
<title>Helena Varno – Qualität und Nachhaltigkeit in der Bildung</title>
<link rel="stylesheet" href="https://fonts.googleapis.com/css2?family=Lato:ital,wght@0,300;0,400;0,700;0,900;1,400&family=Playfair+Display:ital,wght@1,700&display=swap">
<style>
:root{
  --blue:#0e4a7c;
  --blue-dark:#0b3558;
  --green:#93c82a;
  --ink:#1c1c1c;
  --muted:#555;
  --line:#d6d6d6;
  --grey-tab:#6b7782;
  --footer:#f2f2f2;
}
*{box-sizing:border-box;margin:0;padding:0}
html,body{width:1200px;height:2385px;overflow:hidden}
body{position:relative;background:#fff;font-family:'Lato',sans-serif;color:var(--ink)}
.abs{position:absolute}
/* header */
.site-header{position:absolute;left:0;top:0;width:1200px;height:85px;background:#fff;z-index:3}
.brand{position:absolute;left:150px;top:5px;width:79px;height:79px;border:3px solid #222;border-radius:50%;display:flex;align-items:center;justify-content:center;font-weight:900;font-size:12px;letter-spacing:-.2px;color:#222}
.nav a{position:absolute;top:33px;font-size:13px;color:#222;text-decoration:none}
.nav .active::after{content:"";position:absolute;left:-10px;right:-10px;top:49px;height:3px;background:var(--green)}
.btn-call{position:absolute;left:878px;top:22px;width:172px;height:36px;background:var(--green);color:#1a1a1a;font-size:14px;display:flex;align-items:center;justify-content:center;gap:8px;border-radius:2px}
/* hero */
.hero{position:absolute;left:0;top:85px;width:1200px;height:451px;background:linear-gradient(160deg,#2a5d92 0%,#174675 45%,#0c3157 100%)}
.hero-name{position:absolute;left:142px;top:140px;font-family:'Playfair Display',serif;font-style:italic;font-weight:700;font-size:150px;line-height:1;color:#fff;transform:scaleX(.62);transform-origin:left top;white-space:nowrap;letter-spacing:2px;z-index:2}
.hero-sub{position:absolute;left:148px;top:272px;font-weight:300;font-size:46px;line-height:53px;color:#fff;z-index:2}
.hero-tag{position:absolute;left:150px;top:383px;width:540px;height:31px;background:var(--blue-dark);color:#fff;font-size:13.5px;letter-spacing:1px;display:flex;align-items:center;justify-content:center;z-index:2}
.hero-call{position:absolute;left:150px;top:435px;width:221px;height:44px;background:#dfe4ea;border:1px solid #fff;color:#1c2a3a;font-weight:700;font-size:17px;display:flex;align-items:center;justify-content:center;gap:12px;z-index:2}
.portrait-hero{position:absolute;left:790px;top:75px;width:270px;height:461px;background:linear-gradient(180deg,#8b8f95 0%,#6d7178 55%,#9aa0a6 100%);border-radius:120px 120px 0 0;z-index:2}
/* about */
.section-title{position:absolute;left:0;width:1200px;text-align:center;font-weight:900;color:var(--blue)}
.about-lead{position:absolute;left:221px;top:663px;width:759px;font-style:italic;font-size:15.5px;line-height:23px;text-align:justify;color:#111}
.tab{position:absolute;top:735px;width:184px;height:37px;color:#fff;font-size:14px;display:flex;align-items:center;justify-content:center}
.tab.on{left:227px;background:var(--blue)}
.tab.off{left:422px;background:var(--grey-tab)}
.panel{position:absolute;left:218px;top:772px;width:765px;height:532px;border:1px solid var(--line);border-radius:2px;background:#fff}
.job{position:absolute;font-size:13px;line-height:17px;color:#111}
.job .role{display:block;margin:4px 0;color:var(--blue);font-weight:700;font-size:15px}
.job p{margin-top:20px;width:680px;line-height:20px}
.divider{position:absolute;left:33px;width:698px;height:1px;background:var(--line)}
.badge{position:absolute;left:272px;top:220px;width:92px;height:44px;border:1px solid #e2e2e2;background:#f7f7f7}
/* services */
.services{position:absolute;left:0;top:1367px;width:1200px;height:545px;background:linear-gradient(90deg,#8a8780 0%,#a39d92 45%,#9c978d 100%)}
.portrait-services{position:absolute;left:200px;top:0;width:310px;height:545px;background:linear-gradient(180deg,#4b443d 0%,#2d2a28 50%,#3f3a36 100%);border-radius:140px 140px 0 0}
.services h2{position:absolute;left:528px;top:35px;font-weight:900;font-size:48px;color:var(--blue);line-height:1}
.services .lead{position:absolute;left:528px;top:96px;font-size:16px;color:#111}
.services .text{position:absolute;left:528px;top:130px;width:522px;font-size:13px;line-height:20.5px;text-align:justify;color:#111}
.card{position:absolute;width:242px;height:111px;background:#1d1f22;color:#fff;font-weight:700;font-size:19px;line-height:22px;text-align:center;display:flex;align-items:center;justify-content:center}
.card::before{content:"";position:absolute;inset:8px;border:1px solid rgba(255,255,255,.25)}
.card.left-text{text-align:left;justify-content:flex-start;padding-left:17px}
/* contact */
.brand.small{left:203px;top:1982px}
.contact-line{position:absolute;left:204px;font-size:13px;color:#333;display:flex;align-items:center;gap:11px;letter-spacing:.3px}
.field{position:absolute;width:255px;height:39px;border:1px solid #cfcfcf;font-size:11.5px;color:#888;padding:10px 17px;letter-spacing:.3px}
.btn-send{position:absolute;left:794px;top:2181px;width:255px;height:39px;background:var(--green);color:#fff;font-weight:700;font-size:15px;display:flex;align-items:center;justify-content:center;gap:10px}
/* footer */
.site-footer{position:absolute;left:0;top:2303px;width:1200px;height:82px;background:var(--footer)}
.site-footer .copy{position:absolute;left:150px;top:32px;font-size:13px;color:#666}
.social{position:absolute;top:30px;width:16px;height:16px;border:1.6px solid #333;border-radius:4px}
</style>
</head>
<body>

<header class="site-header">
  <div class="brand">HELENA VARNO</div>
  <nav class="nav">
    <a class="active" style="left:530px">Über mich</a>
    <a style="left:630px">Meine Leistungen</a>
    <a style="left:771px">Kontakt</a>
  </nav>
  <div class="btn-call">
    <svg width="14" height="14" viewBox="0 0 24 24" fill="none" stroke="#1a1a1a" stroke-width="2"><path d="M5 3h4l2 5-3 2a12 12 0 0 0 6 6l2-3 5 2v4a2 2 0 0 1-2 2A17 17 0 0 1 3 5a2 2 0 0 1 2-2z"/></svg>
    +49 160 4471 2093
  </div>
</header>

<section class="hero" role="img" aria-label="Foto einer Gruppe junger Lernender in Blau getönt"></section>
<div class="portrait-hero" role="img" aria-label="Porträtfoto der Beraterin mit verschränkten Armen"></div>
<div class="hero-name">HELENA VARNO</div>
<div class="hero-sub">EFQM, Qualitätsmanagement,<br>Nachhaltigkeitsmanagement</div>
<div class="hero-tag">für Volkshochschulen und andere Institutionen der Erwachsenenbildung</div>
<div class="hero-call">
  <svg width="18" height="18" viewBox="0 0 24 24" fill="none" stroke="#1c2a3a" stroke-width="1.8"><path d="M5 3h4l2 5-3 2a12 12 0 0 0 6 6l2-3 5 2v4a2 2 0 0 1-2 2A17 17 0 0 1 3 5a2 2 0 0 1 2-2z"/></svg>
  +49 160 4471 2093
</div>

<h1 class="section-title" style="top:593px;font-size:50px">Über mich</h1>
<p class="about-lead">Selbstständig, Verantwortlich Ressourcen schonen - Beratung zu Nachhaltigkeit &amp; Qualität, Helena Varno - Qualität und Nachhaltigkeit in der Bildung</p>

<div class="tab on">Professional experience</div>
<div class="tab off">Educational background</div>

<div class="panel">
  <div class="job" style="left:43px;top:36px">
    <b>Current</b> 8 months, since May 2022
    <span class="role">Verantwortlich Ressourcen schonen - Beratung zu Nachhaltigkeit &amp; Qualität</span>
    Helena Varno - Qualität und Nachhaltigkeit in der Bildung
    <p>Volkshochschulen und andere Bildungsinstitutionen sichern unsere Zukunft. Auch indem sie verantwortlich mit Energie und anderen Ressourcen umgehen. Ich unterstütze dabei, eine qualitätsgesicherte Nachhaltigkeit praktisch umzusetzen und damit lehrend und Beispiel gebend voranzugehen.</p>
  </div>

  <div class="job" style="left:44px;top:215px">8 months, Mar 2021 - Oct 2021<span class="role">Leiterin Mehrgenerationenhaus</span>Stadt Lindach</div>
  <div class="badge" role="img" aria-label="Partnerabzeichen"></div>
  <div class="job" style="left:459px;top:215px">10 years and 5 months, Oct 2010 - Feb 2021<span class="role">Geschäftsführerin</span>Volkshochschule Ostberg e.V.</div>

  <div class="divider" style="top:300px"></div>
  <div class="job" style="left:49px;top:312px">7 years and 7 months, Mar 2003 - Sep 2010<span class="role">Dozentin für Betriebswirtschaft und Marketing</span>Bildungswerk Talheim</div>
  <div class="job" style="left:459px;top:312px">1 year and 9 months, Feb 2001 - Oct 2002<span class="role">Communication Managerin E-Commerce</span>Feldmark AG, Triesen, Liechtenstein</div>

  <div class="divider" style="top:397px"></div>
  <div class="job" style="left:49px;top:409px">2 years and 9 months, Apr 1998 - Dec 2000<span class="role">Assistenz der Verkaufsleitung</span>Holmer Vertriebs GmbH</div>
  <div class="job" style="left:459px;top:409px">6 months, Oct 1997 - Mar 1998<span class="role">Assistenz der Geschäftsführung</span>Holmer Vertriebs GmbH</div>
</div>

<section class="services" role="img" aria-label="Foto einer Holzwand und Betonmauer als Hintergrund">
  <div class="portrait-services" role="img" aria-label="Foto der Beraterin in Lederjacke vor einer Holzwand"></div>
  <h2>Meine Leistungen</h2>
  <div class="lead">Verantwortlich Ressourcen schonen - Beratung zu Nachhaltigkeit &amp; Qualität</div>
  <p class="text">Volkshochschulen und andere Bildungsinstitutionen sichern unsere Zukunft. Auch indem sie verantwortlich mit Energie und anderen Ressourcen umgehen. Ich unterstütze dabei, eine qualitätsgesicherte Nachhaltigkeit praktisch umzusetzen und damit lehrend und Beispiel gebend voranzugehen.</p>
  <div class="card" style="left:529px;top:241px" role="img" aria-label="Dunkles Bild mit Diagrammen">EFQM</div>
  <div class="card" style="left:807px;top:241px" role="img" aria-label="Dunkles Bild mit Sternen">Qualitäts-<br>management</div>
  <div class="card" style="left:529px;top:378px;background:#1d2a1c" role="img" aria-label="Dunkles Bild mit Pflanze">Nachhaltigkeits-<br>management</div>
  <div class="card left-text" style="left:807px;top:378px" role="img" aria-label="Dunkles Bild mit Lernenden">für Volkshochschulen<br>und andere Institutionen<br>der Erwachsenenbildung</div>
</section>

<div class="brand small">HELENA VARNO</div>
<div class="contact-line" style="top:2081px">
  <svg width="16" height="16" viewBox="0 0 24 24" fill="none" stroke="#333" stroke-width="1.6"><path d="M22 2 2 10l8 3 3 9z M10 13l12-11"/></svg>
  info@varno-beratung.de
</div>
<div class="contact-line" style="top:2111px">
  <svg width="16" height="16" viewBox="0 0 24 24" fill="none" stroke="#333" stroke-width="1.6"><path d="M5 3h4l2 5-3 2a12 12 0 0 0 6 6l2-3 5 2v4a2 2 0 0 1-2 2A17 17 0 0 1 3 5a2 2 0 0 1 2-2z"/></svg>
  +49 160 4471 2093
</div>
<div class="contact-line" style="top:2146px;gap:7px">
  <svg width="15" height="18" viewBox="0 0 24 28"><path d="M12 0a10 10 0 0 0-10 10c0 8 10 18 10 18s10-10 10-18A10 10 0 0 0 12 0zm0 14a4 4 0 1 1 0-8 4 4 0 0 1 0 8z" fill="#222"/></svg>
  Lindach, Germany
</div>

<div class="field" style="left:523px;top:1993px">Vorname</div>
<div class="field" style="left:794px;top:1993px">Nachname</div>
<div class="field" style="left:523px;top:2046px">Email</div>
<div class="field" style="left:794px;top:2046px">Telefon</div>
<div class="field" style="left:523px;top:2099px;width:526px;height:69px">Kommentare</div>
<div class="btn-send">
  <svg width="16" height="16" viewBox="0 0 24 24" fill="none" stroke="#fff" stroke-width="1.8"><path d="M22 2 2 10l8 3 3 9z M10 13l12-11"/></svg>
  SENDEN
</div>

<footer class="site-footer">
  <div class="copy">@2022. varno-beratung.de</div>
  <span class="social" style="left:968px" aria-label="Soziales Netzwerk"></span>
  <span class="social" style="left:1001px" aria-label="Soziales Netzwerk"></span>
  <span class="social" style="left:1034px" aria-label="Videokanal"></span>
</footer>

</body>
</html>
```